Now Open Poster

We need a banner for our sports supplement and nutritional store, Harbor Nutrition.
We were hoping for some sort of creative word art piece.
I have drawn my own mock up just to give you all a very basic starting point. But you are free to go with whatever you feel will work best.
The primary objective is simply to explain a little about what the company does, and then direct traffic towards the store with an 'Open Arrow' pointing left.
Text words we have chosen are:
Protein
Creatine
Health
Fitness
Sports Science
Nutrition
Energy
Achievement
Amino Acids
Organic
Supplements
Performance
Testosterone Support
Vitamins
Growth
Diet
Happiness
Weight Loss
Strong
Natural
Vitality
Accomplished
Below the word art we want our logo (See attached options)
Then below the logo the phrase "Success Starts Here"
Dimensions of the poster are 140cm x 60cm.
Colours: Blues/Whites/Greys/Blacks (Lots of white space please)
Here are some cool pieces I found that had some interesting elements that I liked (I'd love to see a mash-up of styles with a street art feel to it. Something funky!):
http://www.moodgrove.example/pin/804417263190552871/
http://www.moodgrove.example/pin/615380924471208539/
http://www.moodgrove.example/pin/804417263192736155/
http://www.moodgrove.example/pin/804417263194418620/
http://www.moodgrove.example/pin/937162048856301742/
Thanks for reading, message me if you have any further questions!
- Tobias

```html
<!DOCTYPE html>
<html lang="en">
<head>
<meta charset="utf-8">
<title>Harbor Nutrition – Now Open Banner</title>
<link rel="stylesheet" href="https://fonts.googleapis.com/css2?family=Merriweather:wght@900&family=Roboto+Slab:wght@300&family=Courgette&family=Oswald:wght@300;400;500&family=Roboto+Condensed:wght@700&family=Exo+2:ital,wght@1,800&family=Raleway:wght@200;300;400&family=Michroma&family=Archivo+Narrow:wght@500&family=Teko:wght@500&family=Arvo:wght@700&family=Nunito:wght@800&family=Audiowide&family=Lobster+Two&family=Alfa+Slab+One&family=Roboto:wght@700&family=Kaushan+Script&family=Yellowtail&display=swap">
<style>
  :root {
    --page-bg: #2f3b48;
    --banner-white: #ffffff;
    --sky-blue: #1a63b4;
    --band-blue: #1a78c2;
    --navy: #1d3f90;
    --deep-blue: #1d4a96;
    --mid-blue: #1e6fc0;
    --soft-blue: #3a7ac8;
    --bright-blue: #2a86d0;
    --cyan: #21a8e0;
    --light-blue: #5bb8e8;
    --indigo: #2a3080;
    --tag-red: #e0201f;
    --arrow-light: #a6e05a;
    --arrow-dark: #2f9a2a;
  }
  * { margin: 0; padding: 0; box-sizing: border-box; }
  html, body { width: 1200px; height: 1200px; overflow: hidden; background: var(--page-bg); }
  .banner {
    position: absolute; left: 351px; top: 16px;
    width: 498px; height: 1167px;
    background: linear-gradient(to bottom, var(--sky-blue) 0, #6f9fd6 95px, #dfe9f6 205px, var(--banner-white) 310px);
    overflow: hidden;
  }
  .banner-art { display: block; width: 100%; height: 100%; }

  .headline-open { font-family: "Merriweather", serif; font-weight: 900; font-size: 80px; fill: var(--banner-white); }

  .w-creatine { font-family: "Roboto Slab", serif; font-weight: 300; font-size: 36px; fill: var(--soft-blue); }
  .w-protein { font-family: "Courgette", cursive; font-size: 28px; fill: var(--bright-blue); }
  .w-fitness { font-family: "Oswald", sans-serif; font-weight: 400; font-size: 60px; fill: var(--mid-blue); }
  .w-sports { font-family: "Roboto Condensed", sans-serif; font-weight: 700; font-size: 50px; fill: var(--navy); }
  .w-health { font-family: "Exo 2", sans-serif; font-style: italic; font-weight: 800; font-size: 34px; fill: var(--light-blue); }
  .w-science { font-family: "Roboto Condensed", sans-serif; font-weight: 700; font-size: 50px; fill: var(--mid-blue); }
  .w-weight { font-family: "Raleway", sans-serif; font-weight: 200; font-size: 30px; fill: #5aa7dc; }
  .w-energy { font-family: "Michroma", sans-serif; font-size: 22px; fill: var(--mid-blue); }
  .w-achievement { font-family: "Archivo Narrow", sans-serif; font-weight: 500; font-size: 52px; fill: #1b55a8; }
  .w-performance { font-family: "Teko", sans-serif; font-weight: 500; font-size: 54px; fill: var(--navy); }
  .w-amino { font-family: "Arvo", serif; font-weight: 700; font-size: 28px; fill: var(--cyan); }
  .w-diet { font-family: "Oswald", sans-serif; font-weight: 300; font-size: 42px; fill: var(--bright-blue); }
  .w-organic { font-family: "Nunito", sans-serif; font-weight: 800; font-size: 37px; fill: var(--indigo); }
  .w-supplements { font-family: "Audiowide", sans-serif; font-size: 27px; fill: var(--banner-white); stroke: var(--cyan); stroke-width: 1.6px; paint-order: stroke fill; }
  .w-testosterone { font-family: "Oswald", sans-serif; font-weight: 300; font-size: 40px; fill: var(--deep-blue); }
  .w-growth { font-family: "Roboto Condensed", sans-serif; font-weight: 700; font-size: 44px; fill: var(--mid-blue); }
  .w-support { font-family: "Oswald", sans-serif; font-weight: 300; font-size: 36px; fill: var(--deep-blue); }
  .w-vitamins { font-family: "Roboto", sans-serif; font-weight: 700; font-size: 21px; fill: var(--bright-blue); }
  .w-happiness { font-family: "Lobster Two", cursive; font-size: 34px; fill: var(--light-blue); }
  .w-strong { font-family: "Oswald", sans-serif; font-weight: 500; font-size: 46px; fill: #1a5fb0; }
  .w-vitality { font-family: "Alfa Slab One", serif; font-size: 26px; fill: var(--navy); }
  .w-nutrition { font-family: "Raleway", sans-serif; font-weight: 300; font-size: 32px; fill: var(--soft-blue); }
  .w-natural { font-family: "Raleway", sans-serif; font-weight: 400; font-size: 38px; fill: var(--deep-blue); }
  .w-accomplished { font-family: "Kaushan Script", cursive; font-size: 42px; fill: var(--deep-blue); }

  .brand-band { fill: var(--band-blue); }
  .brand-name { font-family: "Nunito", sans-serif; font-weight: 800; font-size: 17px; fill: var(--banner-white); }
  .brand-dot { fill: var(--banner-white); }
  .tagline-text { font-family: "Yellowtail", cursive; font-size: 28px; fill: var(--tag-red); }
  .tagline-swoosh { fill: var(--tag-red); }
</style>
</head>
<body>
  <main class="banner" aria-label="Harbor Nutrition now open banner">
    <svg class="banner-art" viewBox="0 0 366 858" preserveAspectRatio="none">
      <defs>
        <linearGradient id="arrowGreen" x1="0" y1="0" x2="1" y2="1">
          <stop offset="0" stop-color="#a6e05a"/>
          <stop offset="1" stop-color="#2f9a2a"/>
        </linearGradient>
      </defs>

      <text class="headline-open" x="57" y="98" textLength="230" lengthAdjust="spacingAndGlyphs">OPEN</text>
      <g class="open-arrow" aria-label="Arrow pointing left">
        <path d="M282 70 C322 92 318 128 262 132" fill="none" stroke="url(#arrowGreen)" stroke-width="18" stroke-linecap="round"/>
        <polygon points="266,110 196,122 262,154" fill="url(#arrowGreen)"/>
      </g>

      <g class="word-cloud">
        <text class="w-creatine" transform="translate(72,340) rotate(-90)" textLength="160" lengthAdjust="spacingAndGlyphs">Creatine</text>
        <text class="w-protein" x="73" y="212" textLength="94" lengthAdjust="spacingAndGlyphs">Protein</text>
        <text class="w-fitness" x="169" y="228" textLength="150" lengthAdjust="spacingAndGlyphs">FITNESS</text>
        <text class="w-sports" x="73" y="262" textLength="104" lengthAdjust="spacingAndGlyphs">Sports</text>
        <text class="w-health" x="187" y="270" textLength="138" lengthAdjust="spacingAndGlyphs">Health</text>
        <text class="w-science" x="108" y="310" textLength="130" lengthAdjust="spacingAndGlyphs">Science</text>
        <text class="w-weight" x="75" y="343" textLength="210" lengthAdjust="spacingAndGlyphs">Weight Loss</text>
        <text class="w-energy" transform="translate(315,460) rotate(-90)" textLength="180" lengthAdjust="spacingAndGlyphs">ENERGY</text>
        <text class="w-achievement" x="36" y="386" textLength="249" lengthAdjust="spacingAndGlyphs">Achievement</text>
        <text class="w-performance" transform="translate(75,602) rotate(-90)" textLength="204" lengthAdjust="spacingAndGlyphs">PERFORMANCE</text>
        <text class="w-amino" x="83" y="418" textLength="206" lengthAdjust="spacingAndGlyphs">Amino Acids</text>
        <text class="w-diet" x="85" y="458" textLength="50" lengthAdjust="spacingAndGlyphs">Diet</text>
        <text class="w-organic" x="149" y="455" textLength="136" lengthAdjust="spacingAndGlyphs">Organic</text>
        <text class="w-supplements" x="81" y="492" textLength="240" lengthAdjust="spacingAndGlyphs">SUPPLEMENTS</text>
        <text class="w-testosterone" x="92" y="530" textLength="126" lengthAdjust="spacingAndGlyphs">Testosterone</text>
        <text class="w-growth" x="226" y="538" textLength="100" lengthAdjust="spacingAndGlyphs">Growth</text>
        <text class="w-support" x="83" y="557" textLength="76" lengthAdjust="spacingAndGlyphs">Support</text>
        <text class="w-vitamins" transform="translate(181,655) rotate(-90)" textLength="123" lengthAdjust="spacingAndGlyphs">VITAMINS</text>
        <text class="w-happiness" x="184" y="565" textLength="147" lengthAdjust="spacingAndGlyphs">Happiness</text>
        <text class="w-strong" x="86" y="600" textLength="70" lengthAdjust="spacingAndGlyphs">Strong</text>
        <text class="w-vitality" x="187" y="602" textLength="140" lengthAdjust="spacingAndGlyphs">Vitality</text>
        <text class="w-nutrition" x="31" y="634" textLength="128" lengthAdjust="spacingAndGlyphs">Nutrition</text>
        <text class="w-natural" x="191" y="637" textLength="132" lengthAdjust="spacingAndGlyphs">Natural</text>
        <text class="w-accomplished" x="58" y="676" textLength="239" lengthAdjust="spacingAndGlyphs">Accomplished</text>
      </g>

      <rect class="brand-band" x="0" y="715" width="366" height="63"/>
      <text class="brand-name" x="18" y="755" textLength="114" lengthAdjust="spacingAndGlyphs">Harbor Nutrition</text>
      <circle class="brand-dot" cx="183" cy="749" r="42"/>

      <g class="tagline">
        <path class="tagline-swoosh" d="M70 832 C140 822 220 806 284 784 C230 808 150 826 70 832 Z"/>
        <text class="tagline-text" transform="translate(58,820) rotate(-11)" textLength="222" lengthAdjust="spacingAndGlyphs">Success Starts Here</text>
      </g>
    </svg>
  </main>
</body>
</html>
```